Hydraulics Company Business Card Design

Modern business card design for a hydraulics company.
Our company colours are - black, orange and white.
I would like the following contact details included-
Name
Position
Phone number
Email
Website
Street Address

I have attached our company logo.
I would like the back of the card white.

Thank you.

```html
<!DOCTYPE html>
<html lang="en">
<head>
<meta charset="utf-8">
<title>Tamarack Fluidworks – Business Card</title>
<link rel="stylesheet" href="https://fonts.googleapis.com/css2?family=Arimo:wght@400;700&display=swap">
<style>
  :root {
    --orange: #fe9f1e;
    --white: #ffffff;
    --black: #1f1f1f;
    --backdrop: #5a5a5a;
  }
  * { margin: 0; padding: 0; box-sizing: border-box; }
  html, body {
    width: 1200px; height: 1200px; overflow: hidden;
    background: var(--backdrop);
    font-family: "Arimo", Arial, sans-serif;
  }
  .card {
    position: absolute;
    width: 690px; height: 394px;
    overflow: hidden;
  }
  .card--front { left: 265px; top: 158px; background: var(--white); }
  .card--back  { left: 260px; top: 651px; background: var(--orange); }

  .front__brand-panel {
    position: absolute; left: 0; top: 0; width: 346px; height: 100%;
    background: var(--white);
    display: flex; align-items: center; justify-content: center;
  }
  .front__divider {
    position: absolute; left: 346px; top: 0; width: 8px; height: 100%;
    background: var(--black);
  }
  .front__info-panel {
    position: absolute; left: 355px; top: 0; right: 0; height: 100%;
    background: var(--orange); color: var(--white);
  }

  .wordmark { font-weight: 700; line-height: 1; text-align: right; }
  .wordmark__name { display: block; }
  .wordmark__sub { display: block; letter-spacing: 0.06em; }
  .wordmark--small { color: var(--orange); }
  .wordmark--small .wordmark__name { font-size: 34px; }
  .wordmark--small .wordmark__sub { font-size: 19px; margin-top: 6px; }
  .wordmark--large { color: var(--white); }
  .wordmark--large .wordmark__name { font-size: 66px; }
  .wordmark--large .wordmark__sub { font-size: 37px; margin-top: 12px; }

  .contact-block { position: absolute; left: 19px; top: 97px; }
  .contact-block__name { font-size: 27px; font-weight: 700; letter-spacing: 0.02em; line-height: 1; }
  .contact-block__title { font-size: 15px; margin-top: 4px; }
  .contact-block__address { font-size: 16px; line-height: 21px; margin-top: 20px; }
  .contact-list { list-style: none; margin-top: 14px; }
  .contact-list__item {
    display: flex; align-items: center; gap: 12px;
    font-size: 16px; height: 20.5px;
  }
  .contact-list__icon { width: 14px; height: 14px; flex: none; fill: var(--white); }

  .back__brand {
    position: absolute; inset: 0;
    display: flex; align-items: center; justify-content: center;
    padding-bottom: 20px;
  }
</style>
</head>
<body>
  <section class="card card--front">
    <div class="front__brand-panel">
      <div class="wordmark wordmark--small">
        <span class="wordmark__name">Tamarack</span>
        <span class="wordmark__sub">FLUIDWORKS</span>
      </div>
    </div>
    <div class="front__divider"></div>
    <div class="front__info-panel">
      <div class="contact-block">
        <p class="contact-block__name">ROWAN HALE</p>
        <p class="contact-block__title">President</p>
        <p class="contact-block__address">4120 Alder Street<br>Riverton, Canada 20518</p>
        <ul class="contact-list">
          <li class="contact-list__item">
            <svg class="contact-list__icon" viewBox="0 0 16 16"><path d="M3.5 1.5l2.5 0 1 3.5-1.8 1.3a9 9 0 0 0 4.5 4.5l1.3-1.8 3.5 1v2.5c0 .8-.7 1.5-1.5 1.5C7 14 2 9 2 3c0-.8.7-1.5 1.5-1.5z"/></svg>
            <span>555-210-4873</span>
          </li>
          <li class="contact-list__item">
            <svg class="contact-list__icon" viewBox="0 0 16 16"><path d="M4.5 0.5h7a1 1 0 0 1 1 1v13a1 1 0 0 1-1 1h-7a1 1 0 0 1-1-1v-13a1 1 0 0 1 1-1zm.6 2v10h5.8v-10zM8 13.2a.8.8 0 1 0 0 1.6.8.8 0 0 0 0-1.6z" fill-rule="evenodd"/></svg>
            <span>555-319-6402</span>
          </li>
          <li class="contact-list__item">
            <svg class="contact-list__icon" viewBox="0 0 16 16"><path d="M1 3.5h14v9H1zM1.8 4.3 8 9l6.2-4.7" fill="none" stroke="#fff" stroke-width="1.4"/><path d="M1 4l7 5.3L15 4v8.5H1z"/></svg>
            <span>info@tamarackfluidworks.com</span>
          </li>
          <li class="contact-list__item">
            <svg class="contact-list__icon" viewBox="0 0 16 16"><circle cx="8" cy="8" r="6.5" fill="none" stroke="#fff" stroke-width="1.5"/><path d="M1.5 8h13M8 1.5c2.2 2 2.2 11 0 13M8 1.5c-2.2 2-2.2 11 0 13" fill="none" stroke="#fff" stroke-width="1.2"/></svg>
            <span>www.tamarackfluidworks.com</span>
          </li>
        </ul>
      </div>
    </div>
  </section>

  <section class="card card--back">
    <div class="back__brand">
      <div class="wordmark wordmark--large">
        <span class="wordmark__name">Tamarack</span>
        <span class="wordmark__sub">FLUIDWORKS</span>
      </div>
    </div>
  </section>
</body>
</html>
```